Poetry Book Cover Design Project

Looking for a minimalistic book cover design for a collection of poems. The book title is "Before The Morning Turns To Glass". There are three parts to the book. First covers poetry in the theme of Rage. Second love and desire. The third is strange poems. Essentially the sections are "Rage", "Desire" and the "Strange". The reason for the title "Before The Morning Turns To Glass" is as if someone is writing these till life changes towards the intended outcome as felt in each poem. I want to have the author's name "Nirosha Kulathunge" at the bottom. Ilustration attached.
- Minimalistic

```html
<!DOCTYPE html>
<html lang="en">
<head>
<meta charset="utf-8">
<title>Before The Morning Turns To Glass — Cover Wrap</title>
<link rel="stylesheet" href="https://fonts.googleapis.com/css2?family=Special+Elite&family=EB+Garamond&display=swap">
<style>
  :root {
    --backdrop: #ececec;
    --paper: #ffffff;
    --ink: #111111;
    --body-ink: #222222;
    --bird-red-a: #f0263a;
    --bird-red-b: #e0405c;
    --bird-orange-a: #f08a4e;
    --bird-orange-b: #f5b08c;
    --bird-blue-a: #3f6fa8;
    --bird-blue-b: #e8d4c8;
  }
  * { margin: 0; padding: 0; box-sizing: border-box; }
  html, body {
    width: 899px;
    height: 1200px;
    overflow: hidden;
    background: var(--backdrop);
  }
  .cover-wrap {
    position: absolute;
    left: 14px;
    top: 298px;
    width: 870px;
    height: 603px;
    background: var(--paper);
    box-shadow: 0 2px 8px rgba(0,0,0,0.18);
  }
  .back-blurb {
    position: absolute;
    left: 42px;
    top: 78px;
    width: 313px;
    font-family: "EB Garamond", serif;
    font-size: 10px;
    line-height: 12.7px;
    color: var(--body-ink);
    text-align: justify;
  }
  .spine-title, .spine-author {
    position: absolute;
    left: 435px;
    font-family: "Special Elite", monospace;
    color: var(--ink);
    white-space: nowrap;
    transform: translate(-50%, -50%) rotate(-90deg);
  }
  .spine-title { top: 140px; font-size: 9.5px; }
  .spine-author { top: 459px; font-size: 14px; }
  .front-title {
    position: absolute;
    right: 49px;
    top: 36px;
    text-align: right;
    font-family: "Special Elite", monospace;
    font-size: 36px;
    line-height: 40px;
    color: var(--ink);
    font-weight: 400;
  }
  .front-title span { display: block; }
  .bird {
    position: absolute;
    border-radius: 50% 40% 50% 45%;
  }
  .bird-blue {
    left: 718px; top: 366px; width: 101px; height: 36px;
    background: linear-gradient(100deg, var(--bird-blue-a), var(--bird-blue-b));
  }
  .bird-orange {
    left: 612px; top: 385px; width: 101px; height: 110px;
    background: linear-gradient(150deg, var(--bird-orange-a), var(--bird-orange-b));
  }
  .bird-red {
    left: 505px; top: 461px; width: 83px; height: 108px;
    background: linear-gradient(160deg, var(--bird-red-a), var(--bird-red-b));
  }
  .front-author {
    position: absolute;
    right: 49px;
    top: 544px;
    font-family: "Special Elite", monospace;
    font-size: 15px;
    letter-spacing: 0.5px;
    color: var(--ink);
  }
</style>
</head>
<body>
  <main class="cover-wrap">
    <section class="back-cover">
      <p class="back-blurb">Lorem ipsum dolor sit amet, consectetur adipiscing elit. Donec ligula magna, tempus eu auctor sit amet, pharetra ut velit. Curabitur euismod congue nibh quis feugiat. Vivamus in neque in erat lacinia consectetur. In a rhoncus metus. Sed fringilla eros tellus, finibus lobortis libero mattis ut. Maecenas urna neque, porttitor in mi et, porttitor auctor enim. Donec auctor at dolor sit amet dapibus. Proin luctus imperdiet nisi, in semper dui molestie vitae. Sed semper hendrerit tempor. Phasellus velit est, accumsan et molestie ut, condimentum ac erat. Nam aliquam ultricies leo vitae dictum. Morbi non nisi nec nisl vulputate imperdiet in in purus.</p>
    </section>
    <section class="spine">
      <p class="spine-title">Before The Morning Turns To Glass</p>
      <p class="spine-author">Nirosha Kulathunge</p>
    </section>
    <section class="front-cover">
      <h1 class="front-title">
        <span>Before</span><span>The</span><span>Morning</span><span>Turns</span><span>To</span><span>Glass</span>
      </h1>
      <div class="bird bird-blue" role="img" aria-label="Marbled blue swallow silhouette in flight"></div>
      <div class="bird bird-orange" role="img" aria-label="Marbled orange bird silhouette in flight"></div>
      <div class="bird bird-red" role="img" aria-label="Marbled red swallow silhouette in flight"></div>
      <p class="front-author">Nirosha Kulathunge</p>
    </section>
  </main>
</body>
</html>
```